Meadowlark Homecare
Please use tri-fold design on brochure.
Thank you!
Specific information for the brochure from www.meadowlarkhomecare-example.com that I would like used includes the following headings:
Welcome to Meadowlark Homecare
Caregiver Advantage
Mission
Vision
Values
Our Services
ADLs
IADLs
Life Enrichment
Custom Services
ISP
Who Pays for Services
Insurance

```html
<!DOCTYPE html>
<html lang="en">
<head>
<meta charset="UTF-8">
<title>Meadowlark Homecare – Tri-fold Brochure Inside</title>
<link href="https://fonts.googleapis.com/css2?family=Cinzel:wght@600&family=Open+Sans:wght@400;700&display=swap" rel="stylesheet">
<style>
  :root {
    --paper: #ffffff;
    --backdrop: #ececec;
    --accent-red: #d7262f;
    --accent-red-soft: #f3c6c8;
    --heading-navy: #2b3183;
    --body-grey: #4a4a4a;
    --fold-line: #dcdcdc;
    --photo-light: #eef1f4;
    --photo-mid: #b9c2cc;
  }
  * { box-sizing: border-box; margin: 0; padding: 0; }
  html, body { width: 1200px; height: 901px; overflow: hidden; background: var(--backdrop); }
  .brochure {
    display: flex;
    width: 1200px;
    height: 901px;
    background: var(--paper);
  }
  .panel {
    position: relative;
    width: 400px;
    height: 901px;
    padding: 0 44px;
    border-right: 1px solid var(--fold-line);
    font-family: "Open Sans", sans-serif;
    color: var(--body-grey);
    overflow: hidden;
  }
  .panel:last-child { border-right: none; }
  .top-swoosh { position: absolute; top: 0; left: 0; width: 400px; height: 90px; }
  .panel-heading {
    font-family: "Cinzel", serif;
    font-weight: 600;
    font-size: 22px;
    letter-spacing: 2px;
    color: var(--heading-navy);
    text-align: right;
    padding-bottom: 6px;
    border-bottom: 2px solid var(--accent-red);
    margin-bottom: 14px;
  }
  .services-heading { margin-top: 92px; }
  .body-copy {
    font-size: 13px;
    line-height: 1.6;
    text-align: justify;
    margin-bottom: 8px;
  }
  .service-title {
    display: flex;
    align-items: center;
    gap: 8px;
    font-weight: 700;
    font-size: 15px;
    line-height: 1.3;
    color: var(--heading-navy);
    margin: 14px 0 5px;
  }
  .service-title::before {
    content: "";
    width: 8px; height: 8px;
    background: var(--accent-red);
    border-radius: 50%;
    flex: none;
  }
  /* About panel */
  .about-illustration {
    position: absolute;
    top: 0; left: 0;
    width: 400px; height: 210px;
    background: radial-gradient(ellipse at 58% 48%, #e0464d 0%, #c9242c 22%, #f4dede 42%, #f7f7f7 70%);
  }
  .pulse-line { position: absolute; top: 202px; left: 0; width: 400px; height: 40px; }
  .about-content { position: absolute; top: 252px; left: 44px; right: 44px; }
  .about-content .service-title:first-of-type { margin-top: 4px; }
  /* Middle photo */
  .services-photo {
    position: absolute;
    left: 0; bottom: 0;
    width: 400px; height: 320px;
    background: linear-gradient(160deg, var(--photo-light) 0%, var(--photo-mid) 55%, #8e99a6 100%);
  }
  .photo-edge { position: absolute; left: 0; top: 581px; width: 400px; height: 60px; }
</style>
</head>
<body>
<main class="brochure">

  <section class="panel panel-about">
    <div class="about-illustration" role="img" aria-label="Red heart with a stethoscope resting on it"></div>
    <svg class="pulse-line" viewBox="0 0 400 40" aria-hidden="true">
      <polyline points="0,22 170,22 185,22 195,6 207,36 217,14 226,22 400,22" fill="none" stroke="#d7262f" stroke-width="2"/>
    </svg>
    <div class="about-content">
      <h2 class="panel-heading">About Us</h2>
      <h3 class="service-title">Welcome to Meadowlark Homecare</h3>
      <p class="body-copy">We provide trusted, compassionate care at home, helping seniors and adults with disabilities stay safe, independent and close to the people they love.</p>
      <h3 class="service-title">Caregiver Advantage</h3>
      <p class="body-copy">Our caregivers are screened, trained and supported. We match each one to a client's needs and personality, and stay in close contact with families.</p>
      <h3 class="service-title">Mission</h3>
      <p class="body-copy">To deliver dependable, respectful care that improves daily life for every client we serve.</p>
      <h3 class="service-title">Vision</h3>
      <p class="body-copy">A community where everyone can age with comfort and dignity in their own home.</p>
      <h3 class="service-title">Values</h3>
      <p class="body-copy">Compassion, integrity, reliability and respect guide every visit we make.</p>
    </div>
  </section>

  <section class="panel panel-services">
    <svg class="top-swoosh" viewBox="0 0 400 90" aria-hidden="true">
      <path d="M0,0 H400 V26 C300,10 160,60 0,34 Z" fill="#d7262f"/>
      <path d="M0,44 C160,70 300,20 400,36" fill="none" stroke="#f3c6c8" stroke-width="2"/>
    </svg>
    <h2 class="panel-heading services-heading">Our Services</h2>
    <p class="body-copy">Our services support wellbeing at every stage of life. From a few hours each week to round-the-clock care, we build a schedule around you and your family.</p>
    <h3 class="service-title">ADLs</h3>
    <p class="body-copy">Help with bathing, dressing, grooming, toileting, mobility and safe transfers, always delivered with dignity and respect.</p>
    <h3 class="service-title">IADLs</h3>
    <p class="body-copy">Meal preparation, light housekeeping, laundry, errands, shopping and reminders for medication and appointments.</p>
    <div class="services-photo" role="img" aria-label="Stethoscope and pen lying on medical paperwork"></div>
    <svg class="photo-edge" viewBox="0 0 400 60" aria-hidden="true">
      <path d="M0,0 H400 V20 C270,60 130,0 0,30 Z" fill="#ffffff"/>
      <path d="M0,30 C130,0 270,60 400,20" fill="none" stroke="#d7262f" stroke-width="4"/>
    </svg>
  </section>

  <section class="panel panel-services-more">
    <svg class="top-swoosh" viewBox="0 0 400 90" aria-hidden="true">
      <path d="M0,0 H400 V34 C260,60 120,8 0,26 Z" fill="#d7262f"/>
      <path d="M0,36 C120,18 260,70 400,44" fill="none" stroke="#f3c6c8" stroke-width="2"/>
    </svg>
    <h2 class="panel-heading services-heading">Services</h2>
    <h3 class="service-title">Life Enrichment</h3>
    <p class="body-copy">Companionship, conversation, hobbies, outings and gentle activities that keep the mind active and the spirit bright.</p>
    <h3 class="service-title">Custom Services</h3>
    <p class="body-copy">Respite for family caregivers, post-hospital recovery support, overnight stays and care tailored to unique requests.</p>
    <h3 class="service-title">ISP</h3>
    <p class="body-copy">Each client receives an Individual Service Plan written with the family and reviewed regularly, so care always reflects current needs.</p>
    <h3 class="service-title">Who Pays for Services</h3>
    <p class="body-copy">Care may be paid privately, through long-term care policies, veterans' benefits or approved state programs. We help you review every option.</p>
    <h3 class="service-title">Insurance</h3>
    <p class="body-copy">We work directly with many insurance providers and handle the paperwork, so families can focus on what matters most.</p>
  </section>

</main>
</body>
</html>
```